Varnedo Stationary
Varnedo Stationary - Information Technology
Creative Brief
Modern
Mathieu Ferrand
Associate
Av. Pierre Gandel 42 CH-1207 Geneva
mferrand@varnedo-example.com
www.varnedo-example.com

```html
<!DOCTYPE html>
<html lang="en">
<head>
<meta charset="utf-8">
<title>Varnedo Stationery</title>
<link href="https://fonts.googleapis.com/css2?family=Open+Sans:wght@400;600;700;800&display=swap" rel="stylesheet">
<style>
  :root {
    --stage: #e9e7e3;
    --brand-blue: #2b8ed0;
    --brand-blue-deep: #1c74b6;
    --ink: #1f1f1f;
    --ink-soft: #5c5c5c;
    --rule: #d3d3d3;
    --paper: #ffffff;
    --base-dark: #222428;
  }
  * { margin: 0; padding: 0; box-sizing: border-box; }
  html, body {
    width: 1200px; height: 900px; overflow: hidden;
    background: var(--stage);
    font-family: "Open Sans", Arial, sans-serif;
  }
  .stage { position: relative; width: 1200px; height: 900px; }

  .card {
    position: absolute; left: 320px; width: 560px; height: 320px;
    overflow: hidden;
    box-shadow: 0 10px 24px rgba(0,0,0,0.18);
  }

  /* Front */
  .card-front {
    top: 100px;
    background: radial-gradient(ellipse at 55% 40%, var(--brand-blue) 0%, var(--brand-blue-deep) 100%);
    color: var(--paper);
    display: flex; flex-direction: column; align-items: center; justify-content: center;
  }
  .front-name { font-size: 64px; font-weight: 800; letter-spacing: -1px; line-height: 1; }
  .front-url { margin-top: 12px; font-size: 15px; letter-spacing: 4px; }

  /* Back */
  .card-back { top: 470px; background: var(--paper); }
  .brand {
    position: absolute; left: 48px; top: 112px;
    display: flex; align-items: center; gap: 16px;
  }
  .brand-mark { width: 40px; height: 40px; background: var(--brand-blue); border-radius: 50%; }
  .brand-name { font-size: 46px; font-weight: 800; color: var(--ink); letter-spacing: -1px; }

  .divider { position: absolute; left: 0; top: 0; width: 560px; height: 320px; }

  .contact { position: absolute; left: 330px; top: 44px; }
  .person-name { font-size: 19px; font-weight: 700; color: var(--brand-blue); }
  .person-role { font-size: 14px; font-weight: 700; color: var(--ink); margin-bottom: 10px; }
  .address { font-size: 13px; color: var(--ink-soft); line-height: 1.35; margin-bottom: 6px; }
  .contact-list { list-style: none; }
  .contact-list li {
    display: flex; align-items: center; gap: 8px;
    font-size: 13px; color: var(--ink-soft); line-height: 1.65;
  }
  .contact-list svg { width: 14px; height: 14px; flex: none; fill: var(--brand-blue); }

  .base-band { position: absolute; left: 0; bottom: 0; width: 100%; height: 8px; display: flex; }
  .base-band-blue { width: 64%; background: var(--brand-blue); }
  .base-band-dark { flex: 1; background: var(--base-dark); }
</style>
</head>
<body>
<main class="stage">

  <section class="card card-front">
    <div class="front-name">varnedo</div>
    <div class="front-url">www.varnedo-example.com</div>
  </section>

  <section class="card card-back">
    <svg class="divider" viewBox="0 0 560 320" aria-hidden="true">
      <line x1="318" y1="40" x2="268" y2="250" stroke="var(--rule)" stroke-width="1"/>
    </svg>

    <div class="brand">
      <span class="brand-mark"></span>
      <span class="brand-name">varnedo</span>
    </div>

    <div class="contact">
      <div class="person-name">Mathieu Ferrand</div>
      <div class="person-role">Associate</div>
      <div class="address">Av. Pierre Gandel 42<br>CH-1207 Geneva</div>
      <ul class="contact-list">
        <li>
          <svg viewBox="0 0 16 16" aria-label="Phone"><path d="M3 1h3l1 4-2 1c1 2 2 3 4 4l1-2 4 1v3c0 1-1 2-2 2C6 14 2 10 2 3c0-1 0-2 1-2z"/></svg>
          41 21 555 01 10
        </li>
        <li>
          <svg viewBox="0 0 16 16" aria-label="Mobile"><path d="M5 1h6a1 1 0 0 1 1 1v12a1 1 0 0 1-1 1H5a1 1 0 0 1-1-1V2a1 1 0 0 1 1-1zm1 2v8h4V3zm2 9a1 1 0 1 0 0 2 1 1 0 0 0 0-2z"/></svg>
          41 79 555 02 20
        </li>
        <li>
          <svg viewBox="0 0 16 16" aria-label="Fax"><path d="M4 1h6l2 2v3H4zM2 7h12a1 1 0 0 1 1 1v5a1 1 0 0 1-1 1H2a1 1 0 0 1-1-1V8a1 1 0 0 1 1-1zm2 2v1h3V9z"/></svg>
          33 900 55 03 30
        </li>
        <li>
          <svg viewBox="0 0 16 16" aria-label="Email"><path d="M1 3h14v10H1zm1 1.5V12h12V4.5L8 9z"/></svg>
          mferrand@varnedo-example.com
        </li>
        <li>
          <svg viewBox="0 0 16 16" aria-label="Website"><path d="M8 1a7 7 0 1 0 0 14A7 7 0 0 0 8 1zm-5 7h10v1H3zm0-3h10v1H3zm0 6h10v1H3z"/></svg>
          www.varnedo-example.com
        </li>
      </ul>
    </div>

    <div class="base-band">
      <span class="base-band-blue"></span>
      <span class="base-band-dark"></span>
    </div>
  </section>

</main>
</body>
</html>
```